Wedding and event Photography company.

We need a business card design for a photography company based in Singapore named TamKeza. Our core service offering is wedding photojournalism. We would like to see minimalistic designs that use the colour white. The final design should communicate a sense of ease and reliability.

The attached are a couple of visual reference which i found over the web, i hope it will helps.

Project Brief Update (14th July 2014):
- Please refrain from using any images from the website for the design. The laws and regulations over here does not allow me to distribute my client's images. Thanks!

Target Market(s)

Young and middle aged adults aged 24 - 38. With money to spend =D

Industry/Entity Type

Business

Contact Information for Business Card

Name: Dev Lunor
Designation: Head Photographer
Mobile: +65 81749026
Email: jun@tamkeza.example
Website: www.tamkeza.example

Font styles to use
Other font styles liked:
• Baskerville URW

Colors

Designer to choose colors to be used in the design.

Requirements
Must have
• Must include:
• - The brand TamKeza
• - The logo attached
• - Please help to place the brand TamKeza with the logo according to your preferences.
• - Services
• - Wedding Photography
• - Portraiture
• - Photojournalism
Nice to have
• Looking forward to an elegant and simple design. Please see attached examples!
• Please use Serif Fonts
Should not have
• Please refrain from using dark tones for the majority of the design.
• Please refrain from letterpress and embossing.

```html
<!DOCTYPE html>
<html lang="en">
<head>
<meta charset="utf-8">
<title>TamKeza — Business Card</title>
<link rel="stylesheet" href="https://fonts.googleapis.com/css2?family=Libre+Baskerville:ital,wght@0,400;0,700;1,400&display=swap">
<style>
  :root {
    --page: #ffffff;
    --card: #ffffff;
    --card-edge: #d6d6d6;
    --navy: #1f3259;
    --ink-grey: #5e5e5e;
    --mark-grey: #777777;
    --corner: #c9c9c9;
  }
  * { box-sizing: border-box; margin: 0; padding: 0; }
  html, body {
    width: 947px; height: 1200px; overflow: hidden;
    background: var(--page);
  }
  .canvas {
    position: relative; width: 947px; height: 1200px;
    font-family: "Libre Baskerville", "Baskerville", serif;
  }
  .card {
    position: absolute; top: 476px;
    width: 387px; height: 248px;
    background: var(--card);
    border: 1px solid var(--card-edge);
    box-shadow: 2px 3px 4px rgba(0,0,0,0.18);
  }
  .card--front { left: 54px; }
  .card--back  { left: 506px; }

  .brand {
    position: absolute; left: 0; right: 0; top: 74px;
    text-align: center;
    font-size: 29px; font-weight: 400; color: var(--navy);
    letter-spacing: 0.2px;
  }
  .brand-dot {
    position: absolute; left: 50%; top: 128px;
    width: 14px; height: 14px; margin-left: -7px;
    border-radius: 50%; background: var(--mark-grey);
  }

  .corner { position: absolute; width: 19px; height: 19px; }
  .corner--top-right { right: 36px; top: 27px; border-top: 2px solid var(--corner); border-right: 2px solid var(--corner); }
  .corner--bottom-left { left: 35px; top: 203px; border-bottom: 2px solid var(--corner); border-left: 2px solid var(--corner); }

  .person-name {
    position: absolute; left: 0; right: 0; top: 101px;
    text-align: center;
    font-size: 13px; font-weight: 700; color: var(--ink-grey);
    letter-spacing: 6px;
  }
  .person-role {
    position: absolute; left: 0; right: 0; top: 120px;
    text-align: center;
    font-size: 11px; font-style: italic; color: var(--ink-grey);
    letter-spacing: 5.4px;
  }
  .contact {
    position: absolute; left: 0; right: 0; top: 189px;
    text-align: center;
    font-size: 11.5px; color: var(--ink-grey); letter-spacing: 0.8px;
  }
  .website {
    position: absolute; left: 0; right: 0; top: 208px;
    text-align: center;
    font-size: 11px; font-weight: 700; color: var(--navy); letter-spacing: 1px;
  }
</style>
</head>
<body>
<main class="canvas">
  <section class="card card--front" aria-label="Card front">
    <h1 class="brand">TamKeza</h1>
    <span class="brand-dot" aria-hidden="true"></span>
  </section>

  <section class="card card--back" aria-label="Card back">
    <span class="corner corner--top-right" aria-hidden="true"></span>
    <span class="corner corner--bottom-left" aria-hidden="true"></span>
    <p class="person-name">DEV LUNOR</p>
    <p class="person-role">head photographer</p>
    <p class="contact">+65 81749026 • jun@tamkeza.example</p>
    <p class="website">www.tamkeza.example</p>
  </section>
</main>
</body>
</html>
```